Silver Heron Holdings, LLC Business Card

We need a logo that will be embossed or printed in a singular light color for Business Cards. Would be interested in seeing a Cypress Tree graphic. Our company name is Silver Heron Holdings, LLC. Business Card layout and graphic should project imagine of confidence, integrity and strength.

```html
<!DOCTYPE html>
<html lang="en">
<head>
<meta charset="utf-8">
<title>Silver Heron Holdings, LLC — Business Card</title>
<link href="https://fonts.googleapis.com/css2?family=Roboto+Condensed:wght@400;700&display=swap" rel="stylesheet">
<style>
  :root {
    --page-bg: #f4f3f1;
    --card-dark: #0b0c0e;
    --card-dark-mark: #050506;
    --card-dark-text: #18191b;
    --card-light: #ffffff;
    --card-light-border: #9a9a9a;
    --ink: #111111;
  }
  * { margin: 0; padding: 0; box-sizing: border-box; }
  html, body {
    width: 1200px;
    height: 1000px;
    overflow: hidden;
    background: var(--page-bg);
    font-family: "Roboto Condensed", "Arial Narrow", sans-serif;
  }
  .card-set {
    position: absolute;
    left: 240px;
    top: 205px;
    display: flex;
    gap: 40px;
  }
  .card {
    position: relative;
    width: 340px;
    height: 590px;
  }
  .card--front { background: var(--card-dark); }
  .card--back {
    background: var(--card-light);
    border: 1px solid var(--card-light-border);
    color: var(--ink);
    text-align: center;
  }
  .brand-mark {
    position: absolute;
    left: 50%;
    transform: translateX(-50%);
    border-radius: 50%;
  }
  .card--front .brand-mark {
    top: 340px;
    width: 110px;
    height: 110px;
    background: var(--card-dark-mark);
  }
  .card--back .brand-mark {
    top: 45px;
    width: 100px;
    height: 100px;
    background: var(--ink);
  }
  .company-name {
    position: absolute;
    left: 0;
    right: 0;
    text-align: center;
    font-weight: 700;
    font-size: 16px;
    letter-spacing: 0.5px;
    text-transform: uppercase;
  }
  .card--front .company-name { top: 540px; color: var(--card-dark-text); }
  .card--back .company-name { top: 178px; }
  .office {
    position: absolute;
    left: 0;
    right: 0;
    font-size: 15px;
    line-height: 1.35;
  }
  .office__city { font-weight: 700; }
  .office--first { top: 318px; }
  .office--second { top: 392px; }
  .web-contact {
    position: absolute;
    left: 0;
    right: 0;
    top: 505px;
    font-size: 14px;
    line-height: 1.5;
  }
</style>
</head>
<body>
  <main class="card-set">
    <section class="card card--front" aria-label="Card front">
      <div class="brand-mark"></div>
      <p class="company-name">Silver Heron Holdings, LLC</p>
    </section>
    <section class="card card--back" aria-label="Card back">
      <div class="brand-mark"></div>
      <p class="company-name">Silver Heron Holdings, LLC</p>
      <div class="office office--first">
        <p class="office__city">Wrenfield</p>
        <p class="office__phone">(555)-555-0142</p>
      </div>
      <div class="office office--second">
        <p class="office__city">Marlowe</p>
        <p class="office__phone">(555)-555-0187</p>
      </div>
      <div class="web-contact">
        <p>info@silverheronholdings.com</p>
        <p>www.silverheronholdings.com</p>
      </div>
    </section>
  </main>
</body>
</html>
```